Harlow SMSO Covid-19 Vaccine Advertisement (Digital + Print)

The client is needing an advertisement that will run during Football and Soccer Season to advertise getting vaccinated for the Covid-19 Shot.
Request - Sports theme related, Scoreboard, Teams match up, covid-19 vs texas theme

Client - Harlow County Senior and Mobility Support Office

Various Ad types:
Digital Marketing Insertion Orders
- Door Hanger
- Front Page Note
- Insert Schedule

Print + Digital Insertion Orders
- Print Ads
- Email Marketing
- Banner Ads

Must include: logo and brand colors and 1-888-555-0147, and #RaiseTheBarQP and needs to be an English version and a Spanish Version

Message Ideas to incorporate - a variation - do not use all in one ad
Harlow vs COVID
Let’s win this together!
#VaccineSavesLives
#CancelCOVID
#GetVaccinated
#GetBoosted
#GetProtected

```html
<!DOCTYPE html>
<html lang="en">
<head>
<meta charset="utf-8">
<title>Harlow SMSO – Raise The Bar QP Rack Cards</title>
<link href="https://fonts.googleapis.com/css2?family=Fira+Sans:wght@600;800;900&display=swap" rel="stylesheet">
<style>
  :root{
    --page:#3a3d42;
    --navy-top:#0d2a52;
    --navy-mid:#0a1a33;
    --navy-deep:#07111f;
    --light:#4a8fe0;
    --pitch:#2f7a2a;
    --pitch-dark:#1d4f1c;
    --bar:#1f3d68;
    --bar-edge:#16304f;
    --yellow:#f6d83a;
    --yellow-deep:#e6b81c;
    --olive:#7f7f3a;
    --ink:#0f1a2a;
    --white:#f4f6fb;
    --mark:#8f8ad8;
  }
  *{margin:0;padding:0;box-sizing:border-box}
  html,body{width:1200px;height:900px;overflow:hidden}
  body{background:var(--page);font-family:"Fira Sans",Arial,sans-serif;position:relative}

  .rack-card{position:absolute;top:20px;width:380px;height:860px;overflow:hidden;color:var(--white);box-shadow:0 10px 30px rgba(0,0,0,.45)}
  .rack-card--en{left:190px}
  .rack-card--es{left:630px}

  .stadium-scene{position:absolute;inset:0;
    background:
      radial-gradient(ellipse 70% 22% at 50% 26%, rgba(90,160,240,.55), transparent 70%),
      linear-gradient(180deg,var(--navy-top) 0%,var(--navy-mid) 38%,var(--navy-deep) 62%,#163a2a 76%,var(--pitch) 86%,var(--pitch-dark) 100%);}

  .brand{position:absolute;top:64px;left:0;right:0;text-align:center}
  .brand-dot{width:64px;height:64px;border-radius:50%;background:var(--mark);margin:0 auto 18px}
  .brand-name{font-weight:800;font-size:26px;letter-spacing:1px;color:var(--white)}

  .headline{position:absolute;top:244px;left:0;right:0;text-align:center;font-weight:900;font-size:58px;line-height:1.02;text-transform:uppercase;text-shadow:0 4px 8px rgba(0,0,0,.5)}

  .matchup{position:absolute;top:384px;left:22px;width:336px;height:40px;display:flex;transform:skewY(-3deg)}
  .matchup span{display:flex;align-items:center;justify-content:center;font-weight:900;font-size:20px;color:var(--ink);text-transform:uppercase}
  .team{flex:1;background:linear-gradient(180deg,var(--yellow),var(--yellow-deep))}
  .versus{width:74px;background:var(--olive);color:var(--white)!important;clip-path:polygon(14% 0,100% 0,86% 100%,0 100%);margin:0 -10px;z-index:1}

  .checklist{position:absolute;top:436px;left:26px;width:328px;list-style:none}
  .checklist li{height:38px;margin-bottom:6px;background:var(--bar);border-bottom:2px solid var(--bar-edge);display:flex;align-items:center;padding-left:14px;font-weight:800;font-size:16px;text-transform:uppercase;letter-spacing:.3px}
  .checklist li.rally{color:var(--yellow);justify-content:center;padding-left:0;font-size:17px}
  .tick{width:16px;height:16px;margin-right:12px;flex:none}

  .phone-pill{position:absolute;bottom:26px;left:50%;transform:translateX(-50%);width:270px;height:42px;border-radius:21px;background:linear-gradient(180deg,var(--yellow),var(--yellow-deep));border:3px solid var(--ink);display:flex;align-items:center;justify-content:center;gap:8px;font-weight:800;font-size:24px;color:var(--ink)}
  .phone-icon{width:20px;height:24px}
</style>
</head>
<body>

<section class="rack-card rack-card--en" lang="en">
  <div class="stadium-scene" role="img" aria-label="Night football stadium under floodlights with a soccer ball on the grass pitch"></div>
  <div class="brand"><div class="brand-dot"></div><p class="brand-name">HARLOW SMSO</p></div>
  <h1 class="headline">Raise The<br>Bar QP</h1>
  <div class="matchup"><span class="team">Harlow</span><span class="versus">VS</span><span class="team">Covid</span></div>
  <ul class="checklist">
    <li class="rally">Let’s win this together!</li>
    <li><svg class="tick" viewBox="0 0 16 16"><rect x="1" y="3" width="11" height="11" fill="none" stroke="#f6d83a" stroke-width="1.6"/><path d="M4 8l3 3 7-9" fill="none" stroke="#f6d83a" stroke-width="2"/></svg>Vaccine saves lives</li>
    <li><svg class="tick" viewBox="0 0 16 16"><rect x="1" y="3" width="11" height="11" fill="none" stroke="#f6d83a" stroke-width="1.6"/><path d="M4 8l3 3 7-9" fill="none" stroke="#f6d83a" stroke-width="2"/></svg>Cancel covid</li>
    <li><svg class="tick" viewBox="0 0 16 16"><rect x="1" y="3" width="11" height="11" fill="none" stroke="#f6d83a" stroke-width="1.6"/><path d="M4 8l3 3 7-9" fill="none" stroke="#f6d83a" stroke-width="2"/></svg>Get vaccinated</li>
    <li><svg class="tick" viewBox="0 0 16 16"><rect x="1" y="3" width="11" height="11" fill="none" stroke="#f6d83a" stroke-width="1.6"/><path d="M4 8l3 3 7-9" fill="none" stroke="#f6d83a" stroke-width="2"/></svg>Get boosted</li>
    <li><svg class="tick" viewBox="0 0 16 16"><rect x="1" y="3" width="11" height="11" fill="none" stroke="#f6d83a" stroke-width="1.6"/><path d="M4 8l3 3 7-9" fill="none" stroke="#f6d83a" stroke-width="2"/></svg>Get protected</li>
  </ul>
  <div class="phone-pill"><svg class="phone-icon" viewBox="0 0 20 24"><rect x="3" y="1" width="14" height="22" rx="3" fill="#0f1a2a"/><rect x="6" y="4" width="8" height="13" fill="#f6d83a"/><circle cx="10" cy="20" r="1.3" fill="#f6d83a"/></svg>1-888-555-0147</div>
</section>

<section class="rack-card rack-card--es" lang="es">
  <div class="stadium-scene" role="img" aria-label="Estadio de fútbol nocturno con reflectores y un balón sobre el césped"></div>
  <div class="brand"><div class="brand-dot"></div><p class="brand-name">HARLOW SMSO</p></div>
  <h1 class="headline">Eleva El<br>Listón QP</h1>
  <div class="matchup"><span class="team">Harlow</span><span class="versus">VS</span><span class="team">Covid</span></div>
  <ul class="checklist">
    <li class="rally">¡Ganemos esto juntos!</li>
    <li><svg class="tick" viewBox="0 0 16 16"><rect x="1" y="3" width="11" height="11" fill="none" stroke="#f6d83a" stroke-width="1.6"/><path d="M4 8l3 3 7-9" fill="none" stroke="#f6d83a" stroke-width="2"/></svg>La vacuna salva vidas</li>
    <li><svg class="tick" viewBox="0 0 16 16"><rect x="1" y="3" width="11" height="11" fill="none" stroke="#f6d83a" stroke-width="1.6"/><path d="M4 8l3 3 7-9" fill="none" stroke="#f6d83a" stroke-width="2"/></svg>Cancelar covid</li>
    <li><svg class="tick" viewBox="0 0 16 16"><rect x="1" y="3" width="11" height="11" fill="none" stroke="#f6d83a" stroke-width="1.6"/><path d="M4 8l3 3 7-9" fill="none" stroke="#f6d83a" stroke-width="2"/></svg>Vacunarse</li>
    <li><svg class="tick" viewBox="0 0 16 16"><rect x="1" y="3" width="11" height="11" fill="none" stroke="#f6d83a" stroke-width="1.6"/><path d="M4 8l3 3 7-9" fill="none" stroke="#f6d83a" stroke-width="2"/></svg>Obtenga impulso</li>
    <li><svg class="tick" viewBox="0 0 16 16"><rect x="1" y="3" width="11" height="11" fill="none" stroke="#f6d83a" stroke-width="1.6"/><path d="M4 8l3 3 7-9" fill="none" stroke="#f6d83a" stroke-width="2"/></svg>Protégete</li>
  </ul>
  <div class="phone-pill"><svg class="phone-icon" viewBox="0 0 20 24"><rect x="3" y="1" width="14" height="22" rx="3" fill="#0f1a2a"/><rect x="6" y="4" width="8" height="13" fill="#f6d83a"/><circle cx="10" cy="20" r="1.3" fill="#f6d83a"/></svg>1-888-555-0147</div>
</section>

</body>
</html>
```